Coffee Cocktails Recipe Flips cards

create (12) recipe cards that illustrate the finished beverage, with its description, ingredients, and instructions. each card should be 5"x7" and styled to incorporate brand theme and the cultural elements of the beverage. cards will be used for stuffers in shipments of product, used by bartenders, and digitally shared. Present each drink in glassware that embodies the spirit of the culture it represents, garnishing with flair and a nod to the exotic origins, creating a multisensory experience that'll transport the drinker to distant lands with just one indulgent sip.
The presentation of each drink should reflect the cultural fusion aesthetically, using suggested glassware and garnishes to bring the exotic themes to life. Enjoy crafting these drinks and take your guests on a flavorful voyage around the world with each sip!

Target Market(s)

Consumers and Bars and Restaurants

Industry/Entity Type

coffee and adult beverages

Colors

Designer to choose colors to be used in the design.

Requirements
Must have
• brand alignment, styled to reflect the uniqueness of each recipe
Should not have
• appropriate glassware, garnishments, and images of raw ingredients

```html
<!DOCTYPE html>
<html lang="en">
<head>
<meta charset="utf-8">
<title>Café Mocha Bliss – Recipe Card</title>
<link href="https://fonts.googleapis.com/css2?family=Bebas+Neue&family=Great+Vibes&family=Poppins:wght@400;500&display=swap" rel="stylesheet">
<style>
  :root {
    --page-bg: #b1b1b1;
    --card-dark: #16211f;
    --card-green: #223430;
    --wood: #4a2c1f;
    --wood-dark: #2a1811;
    --sage: #8fb3a0;
    --sage-line: #7fa393;
    --beige: #dccfb2;
    --white: #f4f4f1;
    --ink: #17231f;
  }
  * { margin: 0; padding: 0; box-sizing: border-box; }
  html, body { width: 1200px; height: 954px; overflow: hidden; }
  body { background: var(--page-bg); font-family: "Poppins", sans-serif; }

  .recipe-card {
    position: absolute; left: 278px; top: 27px;
    width: 643px; height: 900px; overflow: hidden;
  }
  .scene-backdrop {
    position: absolute; inset: 0;
    background:
      linear-gradient(180deg, transparent 0 80%, var(--wood) 82%, var(--wood-dark) 100%),
      radial-gradient(ellipse at 60% 10%, #2e413b 0%, var(--card-green) 40%, var(--card-dark) 100%);
  }
  .drink-visual {
    position: absolute; left: 30px; top: 400px; width: 300px; height: 440px;
    border-radius: 30px 30px 40px 40px;
    background: linear-gradient(180deg, #f3f1ec 0%, #e9e6e0 24%, #9a6a3c 38%, #c9a77f 52%, #e3d7c5 66%, #b9b6ae 80%, #8d8a83 100%);
    opacity: .85;
  }

  .title { position: absolute; left: 48px; font-family: "Bebas Neue", sans-serif; line-height: 1; }
  .title-cafe { top: 66px; font-size: 168px; color: var(--white); letter-spacing: 2px; }
  .title-mocha { top: 200px; font-size: 122px; color: var(--sage); letter-spacing: 1px; }
  .title-bliss {
    position: absolute; left: 160px; top: 278px;
    font-family: "Great Vibes", cursive; font-size: 70px; color: var(--beige); line-height: 1;
    white-space: nowrap;
  }

  .description {
    position: absolute; left: 341px; top: 76px;
    font-size: 12.2px; line-height: 14.4px; font-weight: 500; color: var(--white);
    white-space: nowrap;
  }

  .section-heading {
    position: absolute; left: 342px;
    font-family: "Bebas Neue", sans-serif; font-size: 20px; letter-spacing: 5px; color: var(--beige);
  }
  .heading-ingredients { top: 270px; }
  .heading-instructions { top: 432px; }

  .ingredient-list { position: absolute; left: 342px; top: 303px; list-style: none; }
  .ingredient-list li {
    display: flex; align-items: center; gap: 6px;
    height: 18.3px; font-size: 12.3px; color: var(--white); white-space: nowrap;
  }
  .ingredient-list svg { width: 11px; height: 11px; flex: none; }

  .step-list { position: absolute; left: 342px; top: 465px; width: 254px; list-style: none; }
  .step {
    position: relative; height: 40.5px;
    border-left: 1px solid var(--sage-line);
  }
  .step-text {
    position: absolute; left: 6px; top: 0; bottom: 6px; width: 222px;
    display: flex; align-items: center;
    font-size: 10.1px; line-height: 12.3px; color: var(--white);
  }
  .step-rule { position: absolute; left: 0; bottom: 0; width: 232px; height: 8px; overflow: visible; }
  .step-badge {
    position: absolute; right: 0; top: 6px; width: 22px; height: 31px;
    background: var(--sage); color: var(--ink); text-align: center;
    font-family: "Poppins", sans-serif; font-weight: 500;
  }
  .step-badge small { display: block; font-size: 6px; line-height: 9px; padding-top: 2px; }
  .step-badge b { display: block; font-size: 15px; line-height: 15px; font-weight: 500; }

  .brand-mark {
    position: absolute; left: 508px; top: 757px;
    display: flex; align-items: center; gap: 7px;
  }
  .brand-dot { width: 14px; height: 14px; border-radius: 50%; background: #cfcfcc; }
  .brand-name { font-family: "Poppins", sans-serif; font-weight: 500; font-size: 28px; color: #cfcfcc; }
</style>
</head>
<body>
<article class="recipe-card">
  <div class="scene-backdrop" role="img" aria-label="Dark café bar backdrop with bokeh lights above a wooden table"></div>
  <div class="drink-visual" role="img" aria-label="Layered café mocha in a footed glass on a saucer with spoon, cookies and coffee beans, cocoa sifted from above"></div>

  <h1>
    <span class="title title-cafe">CAFÉ</span>
    <span class="title title-mocha">MOCHA</span>
    <span class="title-bliss">Bliss</span>
  </h1>

  <p class="description">Indulge in the balance of bittersweet<br>espresso entwined with rich chocolate<br>syrup to enjoy the luxe texture of the Café<br>Mocha Bliss. Gently pour the espresso into<br>your favorite mug, caress it with the<br>velvety touch of chocolate, and crown the<br>mix with steamed milk as soft as clouds.<br>End with a swirl of whipped cream,<br>graced with a sprinkling of chocolate<br>shavings or a delicate dusting of cocoa<br>powder—your canvas of comfort.</p>

  <h2 class="section-heading heading-ingredients">Ingredients</h2>
  <ul class="ingredient-list">
    <li><svg viewBox="0 0 12 12"><circle cx="6" cy="6" r="5" fill="none" stroke="#dccfb2" stroke-width="1"/><path d="M3.5 6.2l1.8 1.8 3.5-4" fill="none" stroke="#dccfb2" stroke-width="1.1"/></svg>5g Orlo Classic Black Coffee</li>
    <li><svg viewBox="0 0 12 12"><circle cx="6" cy="6" r="5" fill="none" stroke="#dccfb2" stroke-width="1"/><path d="M3.5 6.2l1.8 1.8 3.5-4" fill="none" stroke="#dccfb2" stroke-width="1.1"/></svg>8oz hot water</li>
    <li><svg viewBox="0 0 12 12"><circle cx="6" cy="6" r="5" fill="none" stroke="#dccfb2" stroke-width="1"/><path d="M3.5 6.2l1.8 1.8 3.5-4" fill="none" stroke="#dccfb2" stroke-width="1.1"/></svg>2 tablespoons chocolate syrup</li>
    <li><svg viewBox="0 0 12 12"><circle cx="6" cy="6" r="5" fill="none" stroke="#dccfb2" stroke-width="1"/><path d="M3.5 6.2l1.8 1.8 3.5-4" fill="none" stroke="#dccfb2" stroke-width="1.1"/></svg>Steamed milk</li>
    <li><svg viewBox="0 0 12 12"><circle cx="6" cy="6" r="5" fill="none" stroke="#dccfb2" stroke-width="1"/><path d="M3.5 6.2l1.8 1.8 3.5-4" fill="none" stroke="#dccfb2" stroke-width="1.1"/></svg>Whipped cream</li>
    <li><svg viewBox="0 0 12 12"><circle cx="6" cy="6" r="5" fill="none" stroke="#dccfb2" stroke-width="1"/><path d="M3.5 6.2l1.8 1.8 3.5-4" fill="none" stroke="#dccfb2" stroke-width="1.1"/></svg>Chocolate shavings for garnish</li>
  </ul>

  <h2 class="section-heading heading-instructions">Instructions</h2>
  <ol class="step-list">
    <li class="step"><span class="step-text">Mix 8oz of hot water with one packet Orlo Classic Black Instant Coffee, mix well until</span><svg class="step-rule" viewBox="0 0 232 8"><path d="M0 1H190l5 6 5-6H232" fill="none" stroke="#7fa393"/></svg><span class="step-badge"><small>STEP</small><b>1</b></span></li>
    <li class="step"><span class="step-text">Pour the Coffee into a mug.</span><svg class="step-rule" viewBox="0 0 232 8"><path d="M0 1H190l5 6 5-6H232" fill="none" stroke="#7fa393"/></svg><span class="step-badge"><small>STEP</small><b>2</b></span></li>
    <li class="step"><span class="step-text">Stir in the chocolate syrup until<br>well combined.</span><svg class="step-rule" viewBox="0 0 232 8"><path d="M0 1H190l5 6 5-6H232" fill="none" stroke="#7fa393"/></svg><span class="step-badge"><small>STEP</small><b>3</b></span></li>
    <li class="step"><span class="step-text">Top with steamed milk.</span><svg class="step-rule" viewBox="0 0 232 8"><path d="M0 1H190l5 6 5-6H232" fill="none" stroke="#7fa393"/></svg><span class="step-badge"><small>STEP</small><b>4</b></span></li>
    <li class="step"><span class="step-text">Add a generous dollop of whipped cream.</span><svg class="step-rule" viewBox="0 0 232 8"><path d="M0 1H190l5 6 5-6H232" fill="none" stroke="#7fa393"/></svg><span class="step-badge"><small>STEP</small><b>5</b></span></li>
    <li class="step"><span class="step-text">Garnish with chocolate shavings.</span><svg class="step-rule" viewBox="0 0 232 8"><path d="M0 1H190l5 6 5-6H232" fill="none" stroke="#7fa393"/></svg><span class="step-badge"><small>STEP</small><b>6</b></span></li>
  </ol>

  <div class="brand-mark">
    <span class="brand-dot"></span>
    <span class="brand-name">Orlo</span>
  </div>
</article>
</body>
</html>
```